Taboun Dinner, Dessert and Drinks Menu

We need to redesign our Dinner, Desserts, and Drinks Menus.
I have attached all three menus as pdfs. I have chosen the higher payment option because its a few pages and have removed the refund option
Taboun is the most popular Lebanese Restaurant in Melbourne and is a combination of Great Quality Traditional Food and a clean warm ambiance.
Updates
The main part of the menu is the Banquets Section. We want to push our Banquets.
The main focus of the drinks is Lebanese Wines, Lebanese Beer, Lebanese Drinks. Anything Traditional
For the Coffee Menu,
We will be Adding a Chai Latte, More Flavoured Loose Leaf Teas and Removing the Stick Tea. We will also be adding 4 coffee flavour shots to our menu.
Industry/Entity Type
Restaurant
Look and feel
Each slider illustrates characteristics of the customer's brand and the style your logo design should communicate.

```html
<!DOCTYPE html>
<html lang="en">
<head>
<meta charset="utf-8">
<title>Taboun Lebanese Grill – Desserts, Coffees and Teas</title>
<link href="https://fonts.googleapis.com/css2?family=Open+Sans:wght@400;600;700;800&family=Great+Vibes&display=swap" rel="stylesheet">
<style>
:root{
  --wood:#3b2a20;
  --wood-dark:#241811;
  --paper:#f1ebe0;
  --panel:#fbf8f2;
  --red:#c8281e;
  --green:#7cb53a;
  --ink:#3a332d;
  --muted:#6b625a;
  --white:#ffffff;
}
*{margin:0;padding:0;box-sizing:border-box}
html,body{width:876px;height:1200px;overflow:hidden}
body{background:var(--wood);font-family:"Open Sans",Arial,sans-serif;color:var(--ink);position:relative}
.backdrop{position:absolute;inset:0;background:linear-gradient(135deg,#4a3527 0%,var(--wood) 45%,var(--wood-dark) 100%)}
.hero-photo{position:absolute;left:70px;top:0;width:580px;height:370px;border-radius:0 0 40px 40px;background:radial-gradient(ellipse at 45% 45%,#e6c27a 0%,#c9954a 45%,#8a6a3c 80%,#5b4430 100%)}
.brand{position:absolute;right:0;top:0;width:219px;height:131px;background:var(--white);display:flex;flex-direction:column;align-items:center;justify-content:center;border-bottom:6px solid var(--green)}
.brand-name{font-weight:800;font-size:40px;letter-spacing:2px;color:var(--wood)}
.brand-sub{font-size:13px;font-weight:700;letter-spacing:2px;color:var(--wood);text-transform:uppercase;margin-top:2px}
.menu-title{position:absolute;right:44px;top:150px;font-family:"Great Vibes",cursive;font-size:72px;line-height:1;color:var(--white);white-space:nowrap;padding-right:8px}
.sheet{position:absolute;left:29px;top:365px;width:818px;height:788px;background:var(--paper);box-shadow:0 0 18px rgba(0,0,0,.4)}
.col-desserts{position:absolute;left:22px;top:22px;width:370px}
.col-drinks{position:absolute;left:410px;top:0;width:408px;height:788px;background:var(--panel);padding:22px 24px}
h2{font-size:24px;font-weight:700;color:var(--ink);padding-bottom:8px;border-bottom:3px solid var(--green);margin-bottom:14px}
.item{margin-bottom:14px}
.item-name{font-size:15px;font-weight:700;color:var(--red)}
.item-name .tag{color:var(--ink);font-size:12px;margin-left:14px}
.item-desc{font-size:12px;line-height:1.45;color:var(--muted);margin-top:3px}
.feature{background:var(--white);border-left:4px solid var(--green);padding:8px 10px;margin:0 -10px 14px}
.drink-head{font-size:15px;font-weight:700;color:var(--red);margin:14px 0 4px}
.drink-list{list-style:none;font-size:12px;line-height:1.55;color:var(--muted)}
.drink-block{display:flex;justify-content:space-between;align-items:flex-start}
.thumb{flex:none;width:84px;height:64px;border-radius:50%;background:radial-gradient(circle,#fff 0%,#e9e2d6 55%,#b58a5c 70%,#e6ded0 80%)}
.dessert-photos{position:absolute;left:22px;top:600px;width:370px;display:grid;grid-template-columns:1fr 1fr 1fr;gap:10px}
.dessert-photos div{height:80px;background:linear-gradient(135deg,#e7c78c,#b27c3f);border-radius:4px}
.footer{position:absolute;left:0;bottom:0;width:876px;height:47px;display:flex;align-items:center;justify-content:space-between;padding:0 40px;color:var(--white)}
.phone{display:flex;align-items:center;gap:10px;font-size:22px;font-weight:700}
.address{display:flex;align-items:center;gap:6px;font-size:11px}
</style>
</head>
<body>
<div class="backdrop"></div>
<div class="hero-photo" role="img" aria-label="Photo of baklava pieces on a plate"></div>
<div class="brand"><span class="brand-name">TABOUN</span><span class="brand-sub">Lebanese Grill</span></div>
<div class="menu-title">Menu</div>

<main class="sheet">
  <section class="col-desserts">
    <h2>Desserts</h2>
    <div class="item"><div class="item-name">Baklava - $5.90 (3 Pieces)</div>
      <div class="item-desc">A Middle Eastern delicacy. Baked layers of very thin filo pastry stuffed with chopped cashews and topped with homemade rose syrup.</div></div>
    <div class="item"><div class="item-name">Namoura - $5.90 (3 Pieces)</div>
      <div class="item-desc">Lebanese semolina cake topped with almonds and homemade syrup.</div></div>
    <div class="item feature"><div class="item-name">Layali Lubnan (Lebanese Night) - $6.90</div>
      <div class="item-desc">This is a cold semolina pudding with real home styled taste, topped with hand crushed pistachios, homemade cream, and syrup.</div></div>
    <div class="item"><div class="item-name">Rahat al Halkoum - $5.90 (3 Pieces)</div>
      <div class="item-desc">Lebanese Turkish Delights that are flavoured with rosewater or lemon and served in between traditional round Ganabur biscuits.</div></div>
    <div class="item"><div class="item-name">Halawet el Jebn - $6.90 <span class="tag">TABOUN FAVOURITE</span></div>
      <div class="item-desc">A popular Lebanese dessert made from sweet cheese which is drizzled with homemade rose water syrup then topped with crushed pistachio.</div></div>
  </section>
  <div class="dessert-photos">
    <div role="img" aria-label="Photo of namoura cake squares"></div>
    <div role="img" aria-label="Photo of halawet el jebn rolls"></div>
    <div role="img" aria-label="Photo of Turkish delight biscuits"></div>
  </div>

  <section class="col-drinks">
    <h2>Coffees and Teas</h2>
    <div class="item feature"><div class="item-name">Café Blanc - $3.00</div>
      <div class="item-desc">Café Blanc is a tea-like drink that calms the nerves while stimulating digestion after a particularly rich or heavy meal. Café Blanc is a soothing combination of hot water and orange blossom water.</div></div>
    <div class="drink-head">Lebanese Coffee Tray $3.50</div>
    <div class="drink-block">
      <div><div class="drink-head">Other Available Coffees $3.50</div>
        <ul class="drink-list"><li>Cappuccino</li><li>Café Latte</li><li>Short Macchiato</li><li>Long Macchiato</li><li>Short Black</li><li>Long Black</li><li>Flat White</li></ul></div>
      <div class="thumb" role="img" aria-label="Photo of a cup of coffee" style="margin-top:30px"></div>
    </div>
    <div class="drink-block"><div class="drink-head">Hot Chocolate $4.50</div><div class="thumb" role="img" aria-label="Photo of a hot chocolate" style="height:44px;width:64px;margin-top:8px"></div></div>
    <div class="drink-block">
      <div><div class="drink-head">Traditional Teas $3.50</div>
        <ul class="drink-list"><li>Lebanese Loose Leaf Tea</li><li>Lebanese Mint Tea</li><li>Lebanese Anise Tea</li><li>Lebanese Mountain Tea</li></ul></div>
      <div class="thumb" role="img" aria-label="Photo of a glass of tea" style="margin-top:22px"></div>
    </div>
    <div class="drink-head">Chai Latte</div>
    <ul class="drink-list"><li>More Flavoured Loose Leaf Teas</li></ul>
    <div class="drink-block">
      <div><div class="drink-head">Flavoured Coffee</div>
        <ul class="drink-list"><li>Flavoured Coffee_1</li><li>Flavoured Coffee_2</li><li>Flavoured Coffee_3</li><li>Flavoured Coffee_4</li></ul></div>
      <div class="thumb" role="img" aria-label="Photo of a flavoured coffee" style="margin-top:20px"></div>
    </div>
  </section>
</main>

<footer class="footer">
  <div class="phone">
    <svg width="22" height="22" viewBox="0 0 24 24" aria-hidden="true"><path fill="#fff" d="M6.6 10.8a15.1 15.1 0 0 0 6.6 6.6l2.2-2.2c.3-.3.7-.4 1-.2 1.1.4 2.3.6 3.6.6.6 0 1 .4 1 1V20c0 .6-.4 1-1 1A17 17 0 0 1 3 4c0-.6.4-1 1-1h3.5c.6 0 1 .4 1 1 0 1.3.2 2.5.6 3.6.1.3 0 .7-.2 1z"/></svg>
    +61 3 9000 4127
  </div>
  <div class="address">
    <svg width="12" height="14" viewBox="0 0 24 28" aria-hidden="true"><path fill="#fff" d="M12 0a9 9 0 0 0-9 9c0 7 9 19 9 19s9-12 9-19a9 9 0 0 0-9-9zm0 12.5a3.5 3.5 0 1 1 0-7 3.5 3.5 0 0 1 0 7z"/></svg>
    18 Cedar Lane, Northcote VIC 3070, Australia
  </div>
</footer>
</body>
</html>
```